Stationery Design Project

We are a packaging machinery manufacturer that mainly serve the food industry.
We now require a full set of stationary including name card, envelop, letter paper, and etc. to match our company image. The logo has been awarded in a previous contest which is attached here.
Updates
Project Deadline Extended
Reason: We have extended the deadline. We have adjusted the deadline before launch to avoid confusion but it turns out the new date wasn't implemented by the system. All designers please feel free to submit your design. Thank you!
Target Market(s)
B2B customer, including decision maker in food factories, chemical factories, etc.
Industry/Entity Type
Industry
Colors
Designer to choose colors to be used in the design.
Look and feel
Each slider illustrates characteristics of the customer's brand and the style your logo design should communicate.

```html
<!DOCTYPE html>
<html lang="en">
<head>
<meta charset="utf-8">
<title>Vorenta Packaging Technology – Stationery</title>
<link rel="stylesheet" href="https://fonts.googleapis.com/css2?family=Archivo:wght@800&family=Open+Sans:wght@300;400;600&display=swap">
<style>
  :root{
    --brand-green:#0e6e3f;
    --brand-green-dark:#0b5c34;
    --brand-grey:#a4a6a8;
    --paper:#ffffff;
    --backdrop:#e6e6e6;
    --ink-soft:#6c6f72;
    --shadow:0 6px 16px rgba(0,0,0,.14);
  }
  *{box-sizing:border-box;margin:0;padding:0}
  html,body{width:1200px;height:859px;overflow:hidden}
  body{background:var(--backdrop);position:relative;font-family:"Open Sans",Arial,sans-serif}
  .sheet{position:absolute;box-shadow:var(--shadow);overflow:hidden}

  /* brand lockup */
  .lockup{display:flex;flex-direction:column}
  .lockup__row{display:flex;align-items:center;gap:6px}
  .lockup__mark{background:var(--brand-grey)}
  .lockup__name{font-family:"Archivo",Arial,sans-serif;font-weight:800;letter-spacing:.04em;line-height:1}
  .lockup__tag{font-family:"Archivo",Arial,sans-serif;font-weight:800;letter-spacing:.16em;line-height:1;margin-top:3px}
  .on-green .lockup__name,.on-green .lockup__tag{color:#fff}
  .on-white .lockup__name{color:var(--brand-green)}
  .on-white .lockup__tag{color:var(--brand-grey)}

  /* letterhead */
  .letterhead{left:40px;top:40px;width:340px;height:481px;background:var(--paper)}
  .letterhead .lockup{position:absolute;left:28px;top:26px}
  .letterhead .lockup__mark{width:14px;height:14px}
  .letterhead .lockup__name{font-size:18px}
  .letterhead .lockup__tag{font-size:6.5px}
  .letterhead__footer{position:absolute;left:28px;right:28px;bottom:40px;display:flex;justify-content:space-between;font-size:7px;color:var(--ink-soft)}
  .contact{display:flex;align-items:center;gap:4px;margin-bottom:4px}
  .contact svg{width:8px;height:8px;flex:none}
  .letterhead__band{position:absolute;left:0;right:0;bottom:16px;height:8px;display:flex}
  .letterhead__band .band-grey{width:45%;background:var(--brand-grey)}
  .letterhead__band .band-green{flex:1;background:var(--brand-green)}

  /* folder */
  .folder{left:420px;top:40px;width:340px;height:481px;background:var(--brand-green)}
  .folder .lockup{position:absolute;left:40px;top:60px}
  .folder .lockup__mark{width:34px;height:34px}
  .folder .lockup__name{font-size:44px}
  .folder .lockup__tag{font-size:12.5px}

  /* business cards */
  .card{width:350px;height:200px;background:var(--brand-green)}
  .card--front{left:800px;top:40px}
  .card--front .lockup{position:absolute;left:34px;top:64px}
  .card--front .lockup__mark{width:24px;height:24px}
  .card--front .lockup__name{font-size:32px}
  .card--front .lockup__tag{font-size:9px}
  .card--back{left:800px;top:281px;color:#fff;padding:26px 30px}
  .card__name{font-weight:600;font-size:14px}
  .card__title{font-weight:300;font-size:10px;margin-bottom:16px;opacity:.9}
  .card--back .contact{font-size:10px;font-weight:300;margin-bottom:7px;gap:8px}
  .card--back .contact svg{width:11px;height:11px}
  .card__address{font-size:10px;font-weight:300;margin-top:10px}

  /* envelope front */
  .envelope-front{left:40px;top:560px;width:520px;height:260px;background:var(--brand-green)}
  .envelope-front .lockup{position:absolute;left:34px;top:30px}
  .envelope-front .lockup__mark{width:24px;height:24px}
  .envelope-front .lockup__name{font-size:32px}
  .envelope-front .lockup__tag{font-size:9px}
  .envelope-front__address{position:absolute;left:70px;top:150px;color:#fff;font-size:11px;font-weight:300;line-height:1.4}

  /* envelope back */
  .envelope-back{left:600px;top:560px;width:560px;height:260px;background:var(--paper)}
  .envelope-back__flap{position:absolute;left:0;top:0;width:100%;height:120px}
  .envelope-back__seal{position:absolute;left:268px;top:52px;width:24px;height:24px;background:var(--brand-grey)}
</style>
</head>
<body>

  <!-- Letterhead -->
  <section class="sheet letterhead on-white" aria-label="Letterhead">
    <div class="lockup">
      <div class="lockup__row"><span class="lockup__mark"></span><span class="lockup__name">VORENTA</span></div>
      <span class="lockup__tag">PACKAGING TECHNOLOGY</span>
    </div>
    <div class="letterhead__footer">
      <div>street name, city name,<br>state zip code</div>
      <div>
        <div class="contact"><svg viewBox="0 0 10 10"><circle cx="5" cy="5" r="5" fill="#0e6e3f"/><path d="M3 5.2l1.4 1.4L7.2 3.8" stroke="#fff" fill="none" stroke-width="1.2"/></svg>000 000 000</div>
        <div class="contact"><svg viewBox="0 0 10 10"><circle cx="5" cy="5" r="5" fill="#0e6e3f"/><path d="M3 5.2l1.4 1.4L7.2 3.8" stroke="#fff" fill="none" stroke-width="1.2"/></svg>info@vorenta-pack.com</div>
      </div>
      <div class="contact"><svg viewBox="0 0 10 10"><circle cx="5" cy="5" r="5" fill="#0e6e3f"/><path d="M3 5.2l1.4 1.4L7.2 3.8" stroke="#fff" fill="none" stroke-width="1.2"/></svg>www.vorenta-pack.com</div>
    </div>
    <div class="letterhead__band"><span class="band-grey"></span><span class="band-green"></span></div>
  </section>

  <!-- Presentation folder -->
  <section class="sheet folder on-green" aria-label="Presentation folder">
    <div class="lockup">
      <div class="lockup__row"><span class="lockup__mark"></span><span class="lockup__name">VORENTA</span></div>
      <span class="lockup__tag">PACKAGING TECHNOLOGY</span>
    </div>
  </section>

  <!-- Business card front -->
  <section class="sheet card card--front on-green" aria-label="Business card front">
    <div class="lockup">
      <div class="lockup__row"><span class="lockup__mark"></span><span class="lockup__name">VORENTA</span></div>
      <span class="lockup__tag">PACKAGING TECHNOLOGY</span>
    </div>
  </section>

  <!-- Business card back -->
  <section class="sheet card card--back" aria-label="Business card back">
    <div class="card__name">Employee Name</div>
    <div class="card__title">Job Title</div>
    <div class="contact"><svg viewBox="0 0 10 10"><circle cx="5" cy="5" r="5" fill="#fff"/><path d="M3 5.2l1.4 1.4L7.2 3.8" stroke="#0e6e3f" fill="none" stroke-width="1.2"/></svg>000 000 000</div>
    <div class="contact"><svg viewBox="0 0 10 10"><circle cx="5" cy="5" r="5" fill="#fff"/><path d="M3 5.2l1.4 1.4L7.2 3.8" stroke="#0e6e3f" fill="none" stroke-width="1.2"/></svg>info@vorenta-pack.com</div>
    <div class="contact"><svg viewBox="0 0 10 10"><circle cx="5" cy="5" r="5" fill="#fff"/><path d="M3 5.2l1.4 1.4L7.2 3.8" stroke="#0e6e3f" fill="none" stroke-width="1.2"/></svg>www.vorenta-pack.com</div>
    <div class="card__address">street name, city name, state zip code</div>
  </section>

  <!-- Envelope front -->
  <section class="sheet envelope-front on-green" aria-label="Envelope front">
    <div class="lockup">
      <div class="lockup__row"><span class="lockup__mark"></span><span class="lockup__name">VORENTA</span></div>
      <span class="lockup__tag">PACKAGING TECHNOLOGY</span>
    </div>
    <div class="envelope-front__address">street name, city name,<br>state zip code</div>
  </section>

  <!-- Envelope back -->
  <section class="sheet envelope-back" aria-label="Envelope back">
    <svg class="envelope-back__flap" viewBox="0 0 560 120" preserveAspectRatio="none">
      <path d="M0 0H560V90Q560 120 530 120H30Q0 120 0 90Z" fill="#0e6e3f"/>
    </svg>
    <span class="envelope-back__seal"></span>
  </section>

</body>
</html>
```